Business Card Design for Dovlan Holdings

I need a business card designed for Dovlan Holdings. I would like basic contact info and would like the card to be a bit modern but not childish. We manage several companies so it needs to look very professional. Watermark is cool and a plan logo maybe offset on the other side but I will leave the design up to you. I would like to see both color and grey scale designs. This is my first time using Sketch Harbor so hopefully we get some great results! Future projects available for the selected designer potentially.

Target Market(s)

Dovlan Holdings owns several companies serving the software, real estate and automotive industry

Industry/Entity Type

Business

Contact Information for Business Card

Gregory T. Dovlan
608.291.5537
gregory.t.dovlan@mailvista.example

Font styles to use
Serif

Requirements
Must have
• contact information listed on card details
Nice to have
• I am open to letting you use your creative mind to design the best eye catching cards.

```html
<!DOCTYPE html>
<html lang="en">
<head>
<meta charset="utf-8">
<title>Dovlan Holdings – Business Card</title>
<link rel="stylesheet" href="https://fonts.googleapis.com/css2?family=Arimo:wght@400;700&display=swap">
<style>
  :root {
    --stage: #e6e8eb;
    --card: #ffffff;
    --card-shade: #f1f2f4;
    --brand-blue: #1e9ad6;
    --brand-navy: #2c3f8f;
    --ink: #1f1f1f;
    --rule: #1e9ad6;
  }
  * { box-sizing: border-box; margin: 0; padding: 0; }
  html, body {
    width: 1200px;
    height: 873px;
    overflow: hidden;
    background: var(--stage);
    font-family: "Arimo", Arial, sans-serif;
  }
  .sheet {
    width: 1200px;
    height: 873px;
    display: flex;
    flex-direction: column;
    align-items: center;
    justify-content: center;
    gap: 40px;
  }
  .card {
    position: relative;
    width: 660px;
    height: 377px;
    background: linear-gradient(160deg, var(--card) 0%, var(--card) 55%, var(--card-shade) 100%);
    box-shadow: 0 6px 18px rgba(0,0,0,0.18);
    overflow: hidden;
  }
  .tab {
    position: absolute;
    width: 14px;
    background: var(--brand-blue);
  }
  .tab--upper-right {
    right: 0;
    top: 28px;
    height: 140px;
    border-radius: 10px 0 0 10px;
  }
  .tab--lower-left {
    left: 0;
    bottom: 22px;
    height: 150px;
    border-radius: 0 10px 10px 0;
  }
  .brand {
    position: absolute;
    display: flex;
    align-items: center;
    gap: 12px;
  }
  .brand__dot {
    border-radius: 50%;
    background: var(--brand-navy);
    flex: none;
  }
  .brand__name {
    font-weight: 700;
    color: var(--brand-navy);
    line-height: 1.1;
  }
  /* logo side */
  .card--logo .brand {
    left: 50%;
    top: 50%;
    transform: translate(-50%, -50%);
  }
  .card--logo .brand__dot { width: 64px; height: 64px; }
  .card--logo .brand__name { font-size: 30px; }
  /* contact side */
  .card--contact .brand {
    left: 46px;
    top: 150px;
  }
  .card--contact .brand__dot { width: 50px; height: 50px; }
  .card--contact .brand__name { font-size: 22px; }
  .divider {
    position: absolute;
    left: 300px;
    top: 96px;
    width: 2px;
    height: 178px;
    background: var(--rule);
  }
  .details {
    position: absolute;
    left: 326px;
    top: 100px;
  }
  .details__name {
    font-size: 22px;
    font-weight: 700;
    letter-spacing: 0.5px;
    color: var(--brand-blue);
    text-transform: uppercase;
  }
  .details__title {
    font-size: 14px;
    color: var(--brand-blue);
    margin: 3px 0 0 8px;
  }
  .contact-list {
    list-style: none;
    margin: 30px 0 0 36px;
  }
  .contact-list li {
    display: flex;
    align-items: center;
    gap: 8px;
    font-size: 15px;
    color: var(--ink);
    margin-bottom: 16px;
  }
  .contact-list svg { flex: none; }
</style>
</head>
<body>
<main class="sheet">

  <section class="card card--logo" aria-label="Card back">
    <span class="tab tab--upper-right"></span>
    <span class="tab tab--lower-left"></span>
    <div class="brand">
      <span class="brand__dot"></span>
      <span class="brand__name">Dovlan Holdings</span>
    </div>
  </section>

  <section class="card card--contact" aria-label="Card front">
    <span class="tab tab--upper-right"></span>
    <span class="tab tab--lower-left"></span>
    <div class="brand">
      <span class="brand__dot"></span>
      <span class="brand__name">Dovlan<br>Holdings</span>
    </div>
    <span class="divider"></span>
    <div class="details">
      <h1 class="details__name">Gregory T. Dovlan</h1>
      <p class="details__title">Managing Partner</p>
      <ul class="contact-list">
        <li>
          <svg width="14" height="14" viewBox="0 0 14 14" aria-hidden="true">
            <circle cx="7" cy="7" r="7" fill="var(--brand-blue)"/>
            <path d="M3.5 6.2c0-1 .8-1.7 3.5-1.7s3.5.7 3.5 1.7l-1.3.3-.3-.9H5.1l-.3.9zM4.6 7.2h4.8l.6 2.5H4z" fill="#fff"/>
          </svg>
          608.291.5537
        </li>
        <li>
          <svg width="14" height="14" viewBox="0 0 14 14" aria-hidden="true">
            <circle cx="7" cy="7" r="7" fill="var(--brand-blue)"/>
            <rect x="3.5" y="4.5" width="7" height="5" fill="#fff"/>
            <path d="M3.5 4.5 7 7.3 10.5 4.5" fill="none" stroke="var(--brand-blue)" stroke-width="0.8"/>
          </svg>
          gregory.t.dovlan@mailvista.example
        </li>
      </ul>
    </div>
  </section>

</main>
</body>
</html>
```